new roofing company card

New primary business card for roofing company.

Industry/Entity Type

Residential roofing/Specializing in Asphalt and Standing seam metal roofing

Contact Information for Business Card

Phone number is: 484 672 1058 Email: support@fennridgeroofworks.com website: www.fennridgeroofworks.com

Colors
EB3D1F
EC4F4E
F09395
F8D3D4
FCEDEE

```html
<!DOCTYPE html>
<html lang="en">
<head>
<meta charset="utf-8">
<title>Fennridge Roofworks — Business Card</title>
<link rel="stylesheet" href="https://fonts.googleapis.com/css2?family=Cinzel:wght@400&family=Open+Sans:wght@400&display=swap">
<style>
  :root {
    --page-bg: #969696;
    --brand-red: #c0312a;
    --ink: #222222;
    --paper: #ffffff;
    --rule: #333333;
  }
  * { margin: 0; padding: 0; box-sizing: border-box; }
  html, body { width: 1200px; height: 1000px; overflow: hidden; }
  body { background: var(--page-bg); position: relative; }

  .card {
    position: absolute;
    left: 277px;
    width: 646px;
    height: 371px;
    border-radius: 24px;
    overflow: hidden;
  }
  .card--front { top: 102px; background: var(--brand-red); }
  .card--back  { top: 516px; background: var(--paper); }

  .front-wordmark {
    position: absolute;
    right: 62px;
    top: 268px;
    text-align: center;
    font-family: "Cinzel", serif;
    font-weight: 400;
    color: var(--paper);
    line-height: 1;
  }
  .front-wordmark__name { display: block; font-size: 34px; letter-spacing: 1px; }
  .front-wordmark__sub { display: block; font-size: 17px; margin-top: 8px; letter-spacing: 1px; }

  .back-wordmark {
    position: absolute;
    left: 95px;
    width: 188px;
    top: 120px;
    text-align: center;
    font-family: "Cinzel", serif;
    font-weight: 400;
    color: var(--ink);
    line-height: 1;
  }
  .back-wordmark__mark {
    display: block;
    width: 16px;
    height: 16px;
    margin: 0 auto 14px;
    background: var(--ink);
  }
  .back-wordmark__name { display: block; font-size: 27px; letter-spacing: 0.5px; }
  .back-wordmark__sub { display: block; font-size: 16px; margin-top: 8px; letter-spacing: 1px; }

  .divider {
    position: absolute;
    left: 322px;
    top: 122px;
    width: 1px;
    height: 157px;
    background: var(--rule);
  }

  .contact {
    position: absolute;
    left: 345px;
    width: 240px;
    top: 160px;
    text-align: center;
    font-family: "Open Sans", sans-serif;
    font-size: 15px;
    color: var(--ink);
  }
  .contact__icons { display: flex; justify-content: center; gap: 7px; margin-bottom: 6px; }
  .contact__icons svg { width: 21px; height: 21px; display: block; }
  .contact__line { display: block; line-height: 23px; }
</style>
</head>
<body>
  <section class="card card--front" aria-label="Card front">
    <div class="front-wordmark">
      <span class="front-wordmark__name">FENNRIDGE</span>
      <span class="front-wordmark__sub">ROOFWORKS</span>
    </div>
  </section>

  <section class="card card--back" aria-label="Card back">
    <div class="back-wordmark">
      <span class="back-wordmark__mark"></span>
      <span class="back-wordmark__name">FENNRIDGE</span>
      <span class="back-wordmark__sub">ROOFWORKS</span>
    </div>

    <div class="divider"></div>

    <div class="contact">
      <div class="contact__icons">
        <svg viewBox="0 0 24 24" aria-label="Phone">
          <circle cx="12" cy="12" r="12" fill="var(--brand-red)"/>
          <path d="M8.2 6.5c.6-.4 1.2-.2 1.5.3l1 1.8c.3.5.1 1-.3 1.3l-.7.5c.6 1.5 1.6 2.6 3 3.3l.6-.7c.4-.4.9-.5 1.3-.2l1.8 1.1c.5.3.6.9.2 1.4l-.9 1c-.7.7-1.8.8-2.8.3-2.8-1.4-4.6-3.4-5.7-6.2-.4-1-.2-2 .5-2.6z" fill="#fff"/>
        </svg>
        <svg viewBox="0 0 24 24" aria-label="Mobile">
          <circle cx="12" cy="12" r="12" fill="var(--brand-red)"/>
          <rect x="8.5" y="5.5" width="7" height="13" rx="1.2" fill="none" stroke="#fff" stroke-width="1.4"/>
          <circle cx="12" cy="16.3" r="0.8" fill="#fff"/>
        </svg>
        <svg viewBox="0 0 24 24" aria-label="Email">
          <circle cx="12" cy="12" r="12" fill="var(--brand-red)"/>
          <rect x="6" y="8" width="12" height="8.5" fill="none" stroke="#fff" stroke-width="1.3"/>
          <path d="M6 8l6 5 6-5M6 16.5l4.4-4.2M18 16.5l-4.4-4.2" fill="none" stroke="#fff" stroke-width="1.2"/>
        </svg>
      </div>
      <span class="contact__line">484 672 1058</span>
      <span class="contact__line">support@fennridgeroofworks.com</span>
      <span class="contact__line">www.fennridgeroofworks.com</span>
    </div>
  </section>
</body>
</html>
```